Postcard Design

Mexican Grill quick service prepare to order fresh food. Website : www.sunvalecantina.com.

A sample of a postcard for inspiration is attached.

Target Market(s)

University Students 20-30yrs old

Industry/Entity Type

It Service

```html
<!DOCTYPE html>
<html lang="en">
<head>
<meta charset="utf-8">
<title>Sunvale Cantina Postcard</title>
<link rel="stylesheet" href="https://fonts.googleapis.com/css2?family=Lora:ital,wght@0,700;1,700&family=Open+Sans:ital,wght@0,400;1,800&display=swap">
<style>
  :root {
    --stage: #e9e6df;
    --ink: #0b0b0b;
    --card-white: #ffffff;
    --brand-red: #e3262b;
    --band-light: rgba(255, 255, 255, 0.82);
    --slot-grey: #e4e4e4;
    --food-warm: #c9a070;
    --food-deep: #6b4a2e;
  }
  html, body {
    margin: 0;
    padding: 0;
    width: 900px;
    height: 1200px;
    overflow: hidden;
    background: var(--stage);
  }
  .canvas {
    position: relative;
    width: 900px;
    height: 1200px;
  }
  .postcard {
    position: absolute;
    overflow: hidden;
    box-shadow: 0 6px 16px rgba(0,0,0,0.25);
  }

  /* Front */
  .postcard--front {
    left: 83px; top: 55px;
    width: 735px; height: 475px;
    background: var(--ink);
  }
  .front__photo {
    position: absolute;
    right: 0; top: 0;
    width: 520px; height: 475px;
    background:
      linear-gradient(90deg, var(--ink) 0%, rgba(11,11,11,0) 35%),
      linear-gradient(180deg, #5a5a5a 0%, #3a3a3a 25%, var(--food-warm) 45%, #b98a58 70%, #d98a5a 100%);
  }
  .front__band {
    position: absolute;
    left: 0; top: 190px;
    width: 390px; height: 146px;
    background: linear-gradient(90deg, rgba(110,110,110,0.7), rgba(90,90,90,0.45));
  }
  .brand-name {
    position: absolute;
    margin: 0;
    font-family: "Lora", serif;
    font-weight: 700;
    color: var(--brand-red);
    line-height: 1;
    white-space: nowrap;
  }
  .brand-name__line { display: block; }
  .front__brand { left: 30px; top: 95px; font-size: 30px; }
  .front__headline {
    position: absolute;
    left: 30px; top: 196px;
    margin: 0;
    line-height: 1;
  }
  .headline__fast {
    display: block;
    font-family: "Open Sans", sans-serif;
    font-style: italic;
    font-weight: 800;
    font-size: 58px;
    color: var(--card-white);
    letter-spacing: -1px;
  }
  .headline__delicious {
    display: block;
    margin-top: 2px;
    font-family: "Lora", serif;
    font-weight: 700;
    font-size: 70px;
    color: var(--brand-red);
    white-space: nowrap;
  }
  .website {
    position: absolute;
    margin: 0;
    font-family: "Open Sans", sans-serif;
    font-weight: 400;
    color: var(--card-white);
    white-space: nowrap;
  }
  .front__website { left: 25px; top: 381px; font-size: 17px; }

  /* Back */
  .postcard--back {
    left: 102px; top: 643px;
    width: 726px; height: 469px;
    background: var(--card-white);
  }
  .back__photo {
    position: absolute;
    left: 0; top: 0;
    width: 483px; height: 320px;
    background:
      radial-gradient(ellipse at 40% 20%, #e59a4a 0%, rgba(229,154,74,0) 40%),
      linear-gradient(180deg, #f3dcb8 0%, #b7b2ad 30%, var(--food-deep) 70%, #3d3d44 100%);
  }
  .back__band {
    position: absolute;
    left: 0; top: 135px;
    width: 483px; height: 82px;
    background: var(--band-light);
  }
  .back__tagline {
    position: absolute;
    left: 6px; top: 145px;
    margin: 0;
    font-family: "Lora", serif;
    font-weight: 700;
    line-height: 1.15;
    white-space: nowrap;
  }
  .tagline__service { display: block; font-size: 25px; color: var(--ink); }
  .tagline__order { display: block; font-size: 25px; font-style: italic; color: var(--brand-red); }
  .back__footer {
    position: absolute;
    left: 0; top: 300px;
    width: 483px; height: 108px;
    background: linear-gradient(180deg, rgba(11,11,11,0) 0%, var(--ink) 22%);
  }
  .back__website { left: 114px; top: 360px; font-size: 17px; }
  .back__brand { left: 503px; top: 38px; font-size: 18px; line-height: 1.1; }
  .stamp-box {
    position: absolute;
    left: 610px; top: 15px;
    width: 98px; height: 99px;
    background: var(--slot-grey);
  }
  .address-box {
    position: absolute;
    left: 493px; top: 243px;
    width: 211px; height: 121px;
    background: var(--slot-grey);
  }
</style>
</head>
<body>
<main class="canvas">
  <section class="postcard postcard--front">
    <div class="front__photo" role="img" aria-label="Photo of a grilled chicken burrito cut in half"></div>
    <div class="front__band"></div>
    <p class="brand-name front__brand">Sunvale Cantina</p>
    <h1 class="front__headline">
      <span class="headline__fast">FAST FRESH</span>
      <span class="headline__delicious">&amp; DELICIOUS</span>
    </h1>
    <p class="website front__website">sunvalecantina.com</p>
  </section>

  <section class="postcard postcard--back">
    <div class="back__photo" role="img" aria-label="Photo of a plate of tacos with rice and refried beans"></div>
    <div class="back__band"></div>
    <h2 class="back__tagline">
      <span class="tagline__service">MEXICAN GRILL QUICK SERVICE</span>
      <span class="tagline__order">PREPARE TO ORDER FRESH FOOD</span>
    </h2>
    <div class="back__footer"></div>
    <p class="website back__website">sunvalecantina.com</p>
    <p class="brand-name back__brand">
      <span class="brand-name__line">Sunvale</span>
      <span class="brand-name__line">Cantina</span>
    </p>
    <div class="stamp-box"></div>
    <div class="address-box"></div>
  </section>
</main>
</body>
</html>
```